Business Card Design needed for logo design project

Our company needs a Business Card Design. Please refer to our original project in the link above.
Dorian Pellworth
Broker

W: Velvetcrestestates.example
P: 555-302-7184
F: 555-741-2096
E: dorianpellworth@mailbox.example
A: North Dallas Office
Updates

Name Spelling update , sorry Dorian Pellworth card is double sided

```html
<!DOCTYPE html>
<html lang="en">
<head>
<meta charset="utf-8">
<title>Velvetcrest Estates – Business Card</title>
<link rel="stylesheet" href="https://fonts.googleapis.com/css2?family=Arimo:wght@400;700&family=Cinzel:wght@500&display=swap">
<style>
  :root {
    --page: #2a2a2a;
    --card-black: #141414;
    --card-black-light: #262626;
    --card-white: #f4f4f4;
    --accent-green: #17b55a;
    --gold: #c9a063;
    --ink: #1d1d1d;
    --ink-soft: #333333;
  }
  * { box-sizing: border-box; margin: 0; padding: 0; }
  html, body { width: 1200px; height: 900px; overflow: hidden; }
  body {
    background: var(--page);
    font-family: "Arimo", Arial, sans-serif;
    display: flex;
    flex-direction: column;
    align-items: center;
    justify-content: center;
    gap: 50px;
  }
  .card {
    position: relative;
    width: 560px;
    height: 320px;
    border-radius: 18px;
    overflow: hidden;
    box-shadow: 0 10px 30px rgba(0,0,0,.45);
  }

  /* Back side */
  .card-back {
    background: linear-gradient(135deg, var(--card-black-light), var(--card-black) 60%);
  }
  .card-back .edge {
    position: absolute; left: 0; top: 0; bottom: 0; width: 8px;
    background: var(--accent-green);
  }
  .card-back .edge::after {
    content: ""; position: absolute; left: 8px; bottom: 48px;
    border-top: 8px solid transparent; border-bottom: 8px solid transparent;
    border-left: 9px solid var(--accent-green);
  }
  .brand {
    display: flex; align-items: center; gap: 12px;
  }
  .brand-dot {
    width: 14px; height: 14px; border-radius: 50%; background: var(--gold);
  }
  .brand-name {
    font-family: "Cinzel", Georgia, serif;
    font-weight: 500;
    color: var(--gold);
    letter-spacing: .04em;
  }
  .card-back .brand {
    position: absolute; left: 0; right: 0; top: 118px; justify-content: center;
  }
  .card-back .brand-name { font-size: 32px; }
  .card-back .website {
    position: absolute; left: 30px; bottom: 42px;
    color: var(--gold); font-weight: 700; font-size: 16px;
  }

  /* Front side */
  .card-front { display: flex; background: var(--card-white); }
  .front-brand-panel {
    width: 250px; height: 100%;
    background: linear-gradient(160deg, var(--card-black-light), var(--card-black) 70%);
    display: flex; align-items: center; justify-content: center;
    padding: 0 18px;
  }
  .front-brand-panel .brand { flex-direction: column; gap: 10px; text-align: center; }
  .front-brand-panel .brand-name { font-size: 22px; line-height: 1.25; }
  .divider {
    position: relative; width: 9px; background: var(--accent-green);
  }
  .divider::after {
    content: ""; position: absolute; left: 9px; top: 104px;
    border-top: 9px solid transparent; border-bottom: 9px solid transparent;
    border-left: 10px solid var(--accent-green);
  }
  .contact-panel { flex: 1; padding: 78px 0 0 34px; }
  .person-name { font-size: 24px; font-weight: 700; color: var(--ink); }
  .person-role { font-size: 14px; color: var(--gold); margin-top: 3px; }
  .contact-list { list-style: none; margin-top: 26px; }
  .contact-list li {
    display: flex; align-items: center; gap: 8px;
    font-size: 13.5px; color: var(--ink-soft); margin-bottom: 8px;
  }
  .contact-list svg { width: 13px; height: 13px; flex: none; fill: var(--gold); }
</style>
</head>
<body>

  <section class="card card-back" aria-label="Card back">
    <div class="edge"></div>
    <div class="brand">
      <span class="brand-dot"></span>
      <span class="brand-name">Velvetcrest Estates</span>
    </div>
    <p class="website">www.Velvetcrestestates.example</p>
  </section>

  <section class="card card-front" aria-label="Card front">
    <div class="front-brand-panel">
      <div class="brand">
        <span class="brand-dot"></span>
        <span class="brand-name">Velvetcrest Estates</span>
      </div>
    </div>
    <div class="divider"></div>
    <div class="contact-panel">
      <h1 class="person-name">Dorian Pellworth</h1>
      <p class="person-role">Broker</p>
      <ul class="contact-list">
        <li>
          <svg viewBox="0 0 16 16" aria-hidden="true"><rect x="2" y="1" width="12" height="14" rx="2"/><rect x="4" y="3" width="8" height="4" fill="#f4f4f4"/></svg>
          555-302-7184
        </li>
        <li>
          <svg viewBox="0 0 16 16" aria-hidden="true"><rect x="4" y="1" width="8" height="5"/><rect x="1" y="6" width="14" height="6" rx="1"/><rect x="4" y="10" width="8" height="5"/></svg>
          555-741-2096
        </li>
        <li>
          <svg viewBox="0 0 16 16" aria-hidden="true"><rect x="1" y="3" width="14" height="10" rx="1"/><path d="M2 4 L8 9 L14 4" stroke="#f4f4f4" stroke-width="1.5" fill="none"/></svg>
          dorianpellworth@mailbox.example
        </li>
        <li>
          <svg viewBox="0 0 16 16" aria-hidden="true"><circle cx="8" cy="8" r="7"/><path d="M1 8h14M8 1c-3 3-3 11 0 14M8 1c3 3 3 11 0 14" stroke="#f4f4f4" stroke-width="1" fill="none"/></svg>
          www.Velvetcrestestates.example
        </li>
      </ul>
    </div>
  </section>

</body>
</html>
```